Ashworth Web Design Project

I need the front page and an internal page designed for this client's website. The logo is attached. Obviously the colors have to go with and/or work with the logo colors. I also attached a very rough brochure layout to help you see the direction we're going in with print materials. The rough site map is also attached. I see a slider on the homepage, the art for which I may come back to you to create. This clinic is in a very high end Dallas neighborhood. The hook is that it's a primary care and urgent facility with convenient hours.

I don't know how much this impacts your design, but this will be a Wordpress site and I'm using a framework called Struxo (struxo-demo.example). If Struxo proves to be inflexible, I'll have to get a template that allows me to execute your design.

This site (http://oakbendcareclinic.example) has the type and quality of content I will eventually have on the Ashworth site.

I just revised the brief for this project. I added the site map and added details to the overview and the "Must Have" section. Thank you for revisiting the brief. 

Reason: Christmas was a bad time to end it.

Target Market(s)

Women 25-54 with children living at home, income over $150k/year

Industry/Entity Type

Clinic

Requirements
Must have
• Masthead incorporating the logo
Followed by the primary nav
Slider on the home page below that
Dual nav - 1 with the nav in the attached site map
2 secondary nav with areas of healthcare
There will three blocks under the nav
1. It's about time (with a small blurb less than 50 words.
2. It's about choices (with small blurb)
3. It's about you (with small blurb)
Three footer blocks
patient check in link on every page
"No appointment? No problem" icon on every page

```html
<!DOCTYPE html>
<html lang="en">
<head>
<meta charset="utf-8">
<title>Ashworth Medical</title>
<link href="https://fonts.googleapis.com/css2?family=Montserrat:wght@400;500;700&family=Oswald:wght@500;600&family=Noto+Serif:ital@1&display=swap" rel="stylesheet">
<style>
:root{
  --blue:#0a5ea8;
  --blue-dark:#08488a;
  --green:#21a84a;
  --green-text:#2fae55;
  --ink:#333;
  --muted:#555;
  --page-grey:#ededed;
  --card-grey:#e6e6e6;
  --line:#d4d4d4;
  --orange:#f39a1d;
  --footer-grey:#e9e9e9;
  --copy-band:#c9c9c9;
}
*{box-sizing:border-box;margin:0;padding:0}
html,body{width:736px;height:1200px;overflow:hidden}
body{position:relative;background:#fff;font-family:"Montserrat",Arial,sans-serif;color:var(--ink)}
.abs{position:absolute}
a{color:inherit;text-decoration:none}

/* header */
.brand{left:82px;top:22px;display:flex;align-items:center;gap:8px}
.brand-dot{width:42px;height:42px;border-radius:50%;background:var(--blue)}
.brand-name{font-size:24px;font-weight:700;color:var(--blue);letter-spacing:-.5px;line-height:1}
.top-links{left:459px;top:6px;display:flex;gap:18px;font-size:10.5px;color:var(--blue)}
.social-mini{left:597px;top:7px;display:flex;gap:9px}
.social-mini span{width:11px;height:11px;background:var(--blue);border-radius:2px}

/* main nav */
.main-nav{left:86px;top:87px;width:560px;height:22px;background:var(--blue);border-radius:11px;display:flex}
.main-nav a{flex:1;color:#fff;font-size:12px;font-weight:700;display:flex;align-items:center;justify-content:center;border-right:1px solid #3f83c3}
.main-nav a:last-child{border-right:0;flex:1.4}
.main-nav a:first-child{flex:.9}

.band-grey{left:0;top:110px;width:736px;height:524px;background:var(--page-grey)}

/* intro blocks */
.intro{top:118px;height:72px;background:#fff;border:1px solid var(--line);padding:8px 10px}
.intro h3{font-size:13px;font-weight:400;color:var(--blue);margin-bottom:6px}
.intro h3 b{font-weight:500}
.intro p{font-size:7.5px;line-height:12px;color:var(--ink)}

/* slider */
.slider{left:86px;top:200px;width:560px;height:240px;background:linear-gradient(120deg,#dfe6ea 0%,#e4c7a8 40%,#edd7bd 65%,#eef1f2 100%);border:2px solid #fff;box-shadow:0 0 0 1px var(--line)}
.cap-green{left:325px;top:381px;width:317px;height:28px;background:var(--green);color:#fff;font-size:19px;display:flex;align-items:center;padding-left:10px;border-radius:4px 4px 0 4px}
.cap-blue{left:393px;top:409px;width:242px;height:28px;background:var(--blue);color:#fff;font-size:19px;display:flex;align-items:center;padding-left:8px;border-radius:0 0 14px 4px}
.dots{left:341px;top:451px;display:flex;gap:3px}
.dots span{width:8px;height:8px;border-radius:50%;background:#d2d2d2}
.dots span:first-child{background:#999}

/* care nav */
.care-nav{left:86px;top:466px;width:142px;height:158px;background:var(--blue);list-style:none;padding:10px 0 0 10px}
.care-nav li{color:#fff;font-size:9.5px;height:20px;display:flex;align-items:center;gap:7px}
.care-nav li::before{content:"›";font-size:9px;opacity:.8}

.welcome{left:246px;top:464px;width:398px}
.welcome .small{font-size:16px;color:var(--muted)}
.welcome h1{font-size:19px;font-weight:700;color:var(--blue);line-height:22px;margin-bottom:6px}
.welcome p{font-size:9px;line-height:14.3px;color:var(--muted)}

/* content */
.care-head{left:84px;top:659px;font-family:"Oswald",sans-serif;font-size:15px;font-weight:600;color:var(--blue);letter-spacing:.3px}
.care-copy{left:85px;top:686px;width:345px;font-size:9px;line-height:16px;color:var(--muted)}
.care-copy a{color:var(--blue);display:block;margin-top:0}

.doctor{left:469px;top:655px;width:177px;height:175px;background:var(--card-grey);border-radius:3px;padding:9px 11px}
.doc-photo{position:absolute;left:11px;top:9px;width:65px;height:64px;background:linear-gradient(160deg,#c9b6a3,#e8e4e0);border:1px solid #fff}
.doc-name{position:absolute;left:88px;top:6px;font-size:11.5px;color:#222;line-height:13px}
.doc-name small{font-size:9.5px;color:var(--muted)}
.doc-role{position:absolute;left:89px;top:47px;font-size:9px;color:var(--blue);line-height:11px}
.doctor p{position:absolute;left:11px;top:78px;width:158px;font-size:7.6px;line-height:13px;color:var(--muted)}

.sec-title{font-size:14px;color:var(--blue);font-weight:500}
.news{left:85px;top:844px;width:180px}
.news .sec-title{margin-bottom:12px}
.news-item{margin-bottom:10px;font-size:7.5px;line-height:12px}
.news-item .date{color:var(--muted)}
.news-item .title{color:var(--blue);font-size:8.5px}
.news-item p{color:var(--muted)}

.testi{left:277px;top:844px;width:180px}
.quote-mark{position:absolute;left:0;top:30px;width:24px;height:22px}
.testi blockquote{margin:13px 0 0 35px;font-family:"Noto Serif",serif;font-style:italic;font-size:8.6px;line-height:13.2px;color:var(--muted)}
.testi cite{display:block;margin-left:35px;font-style:normal;font-size:8px;color:#222}

.newsletter{left:469px;top:840px;width:177px;height:135px;background:var(--card-grey);border-radius:3px;padding:10px 11px}
.newsletter h4{font-family:"Oswald",sans-serif;font-size:14px;font-weight:500;line-height:15px;color:#111}
.env{position:absolute;right:14px;top:12px}
.newsletter p{margin-top:8px;font-size:7.6px;line-height:11.5px;color:#333}
.subscribe{position:absolute;left:19px;top:102px;width:140px;height:26px;background:linear-gradient(#f8b03c,var(--orange));border-radius:4px;color:#fff;font-size:8px;font-weight:700;display:flex;align-items:center;justify-content:center;box-shadow:0 2px 2px rgba(0,0,0,.2)}

/* footer */
.footer{left:0;top:1005px;width:736px;height:167px;background:linear-gradient(#d9d9d9,var(--footer-grey) 40%,#fafafa)}
.walkin{left:202px;top:1014px;width:320px;height:34px;background:var(--green);border-radius:17px;color:#fff;font-size:19px;display:flex;align-items:center;justify-content:center}
.connect{left:108px;top:1064px;width:108px;text-align:center;font-size:11px;letter-spacing:2.2px;color:#444;line-height:12px}
.social{left:108px;top:1099px;display:flex;gap:13px}
.social span{width:28px;height:28px;background:#7f9bb5;border-radius:3px}
.foot-brand{left:285px;top:1066px;width:162px;text-align:center}
.foot-brand .brand-dot{width:30px;height:30px;margin:0 auto 8px}
.foot-name{font-size:18px;font-weight:700;color:var(--blue);letter-spacing:-.4px}
.contact{left:489px;top:1066px;font-size:7.6px;line-height:12.5px;color:#333}
.contact .phone{font-size:16px;color:var(--green-text);margin-bottom:4px;line-height:20px}
.foot-rule{left:84px;top:1143px;width:562px;height:1px;background:var(--line)}
.foot-nav{left:0;top:1153px;width:736px;display:flex;justify-content:center;gap:19px;font-size:8px;color:#333}
.copy{left:0;top:1172px;width:736px;height:28px;background:var(--copy-band);font-size:7.5px;color:#222;display:flex;align-items:center;justify-content:center}
</style>
</head>
<body>

<header>
  <div class="abs brand">
    <span class="brand-dot"></span>
    <div class="brand-name">AshworthMedical</div>
  </div>
  <nav class="abs top-links"><a>Register</a><a>Log In</a><a>Blog</a></nav>
  <div class="abs social-mini"><span></span><span></span><span></span></div>
  <nav class="abs main-nav">
    <a>Home</a><a>About</a><a>Services</a><a>Staff</a><a>Insurance</a><a>Videos</a><a>Contact Us</a>
  </nav>
</header>

<div class="abs band-grey"></div>

<section>
  <div class="abs intro" style="left:86px;width:183px">
    <h3>It's <b>About Time</b></h3>
    <p>Lorem ipsum dolor sit amet, consectetur adipisicing elit, sed do eiusmod tempor incididunt ut labore.</p>
  </div>
  <div class="abs intro" style="left:279px;width:179px">
    <h3>It's <b>About Choices</b></h3>
    <p>Lorem ipsum dolor sit amet, consectetur adipisicing elit, sed do eiusmod tempor incididunt.</p>
  </div>
  <div class="abs intro" style="left:463px;width:183px">
    <h3>It's <b>About You</b></h3>
    <p>Lorem ipsum dolor sit amet, consectetur adipisicing elit, sed do eiusmod tempor incididunt ut labore et.</p>
  </div>
</section>

<section>
  <div class="abs slider" role="img" aria-label="Photo of a smiling family of four outdoors"></div>
  <div class="abs cap-green">Concierge-quality healthcare...</div>
  <div class="abs cap-blue">...for your whole family</div>
  <div class="abs dots"><span></span><span></span><span></span><span></span><span></span></div>
</section>

<ul class="abs care-nav">
  <li>Immediate Care</li><li>Allergies</li><li>Primary Care</li><li>Women's Health</li>
  <li>Medical Spa Treatments</li><li>Men's Health</li><li>Weight Loss</li>
</ul>

<section class="abs welcome">
  <div class="small">Welcome to</div>
  <h1>AshworthMedical</h1>
  <p>Sed ut perspiciatis unde omnis iste natus error sit voluptatem accusantium doloremque laudantium, totam rem aperiam, eaque ipsa quae ab illo inventore veritatis et quasi architecto beatae vitae dicta sunt explicabo. Nemo enim ipsam voluptatem quia voluptas sit aspernatur aut odit aut fugit, sed quia consequuntur magni dolores eos qui ratione. voluptatem sequi nesciunt. Neque porro quisquam est, qui dolorem ipsum quia dolor sit amet, consectetur, adipisci velit, sed quia non numquam eius modi tempora incidunt ut labore et dolore magnam aliquam quaerat voluptatem.</p>
</section>

<h2 class="abs care-head">CONVENIENT COMPREHENSIVE CARE</h2>
<div class="abs care-copy">
  <p>Your health is important to you. It's impartant to us, too. You're the reason we're here with comprehensive compassionate healthcare services for you and your entire family. We believe to make healthcare really work. it has to start with a relationship based on trust, respect, and understanding. That means we do everything in our power, including extending our hours, to make the time you spend at Ashworth Medical positive and productive.</p>
  <a>Read more...</a>
</div>

<aside class="abs doctor">
  <div class="doc-photo" role="img" aria-label="Portrait of the family physician"></div>
  <div class="doc-name">Dorian K.<br><small>Vance, MD</small></div>
  <div class="doc-role">Your new<br>family physician</div>
  <p>Lorem ipsum dolor sit amet, consectetur adipisicing elit, sed do eiusmod tempor incididunt ut labore et dolore magna aliqua. Ut enim ad minim veniam, quis nostrud exercitation ullamco laboris nisi ut aliquip ex ea commodo consequat.</p>
</aside>

<section class="abs news">
  <h3 class="sec-title">Latest News</h3>
  <div class="news-item">
    <div class="date">10. 12. 2012</div>
    <div class="title">Lorem ipsum dolor sit amet</div>
    <p>Suspendisse ullamcorper molestie enim, eget auctor dolor consequat at.</p>
  </div>
  <div class="news-item">
    <div class="date">10. 12. 2012</div>
    <div class="title">Lorem ipsum dolor sit amet</div>
    <p>Suspendisse ullamcorper molestie enim, eget auctor dolor consequat at.</p>
  </div>
</section>

<section class="abs testi">
  <h3 class="sec-title">Testimonials</h3>
  <svg class="quote-mark" viewBox="0 0 24 22"><path d="M0 0h10v12l-5 10H1l3-10H0zM13 0h10v12l-5 10h-4l3-10h-4z" fill="#c9c9c9"/></svg>
  <blockquote>Lorem ipsum dolor sit amet, consectetur adipisicing elit, sed do eiusmod tempor incididunt ut labore et dolore magna aliqua. Ut enim ad minim veniam, quis nostrud exercitation ullamco laboris nisi ut aliquip ex ea commodo.</blockquote>
  <cite>John Doe</cite>
</section>

<aside class="abs newsletter">
  <h4>Subscribe to<br>Our Newsletter</h4>
  <svg class="env" width="38" height="28" viewBox="0 0 38 28"><rect x="1" y="3" width="36" height="24" fill="#fff" stroke="#bbb"/><path d="M1 3l18 13 18-13" fill="none" stroke="#bbb"/><path d="M1 3h36" stroke="#d33" stroke-width="2" stroke-dasharray="3 3"/></svg>
  <p>Receive announcements, news, events information and many offers from ASHWORTHMEDICAL.EXAMPLE, Inc. in your inbox.</p>
  <a class="subscribe">SUBSCRIBE NOW</a>
</aside>

<footer>
  <div class="abs footer"></div>
  <div class="abs walkin">No appointment? No problem</div>
  <div class="abs connect">CONNECT<br>WITH US</div>
  <div class="abs social"><span></span><span></span><span></span></div>
  <div class="abs foot-brand">
    <div class="brand-dot"></div>
    <div class="foot-name">AshworthMedical</div>
  </div>
  <address class="abs contact" style="font-style:normal">
    <div class="phone">(555) 014 2290</div>
    AshworthFamilyMedical.example<br>
    4120 Linden Ave (at Elm Rd) Ste 180,<br>
    Brookvale, TX 70000
  </address>
  <div class="abs foot-rule"></div>
  <nav class="abs foot-nav"><a>Home</a><a>About</a><a>Services</a><a>Staff</a><a>Insurance</a><a>Videos</a><a>Contact Us</a></nav>
  <div class="abs copy">© 2012 AshworthMedical. All Rights Reserved</div>
</footer>

</body>
</html>
```